We specialize in pizza, pasta and salads and are now offering TAKE & BAKE and GRAB & GO ...

Looking for either a 8.5" x 11" or similar for a instore display. WILL BE ON A SWIVELING HOLDER to catch customers attention.

**THIS IS A DOUBLE SIDED PRINT**

ONE SIDE will consist of WHAT'S FOR DINNER TONIGHT? and the following:
* Take & Bake"
* "Baked Pasta"
* Freshly made in house
* Lasagna
$13.50
- please include attached closeup picture and logo

THE OTHER SIDE will consist of
mini charcutier board.
* snack size charcutier delight *
* Enjoy the flavors of gourmet snacking, all in one convenient box!

PRICE $8.99

Winning design will be commissioned to design labels for "grab and go" for take and bake pasta, charcuterie box, pasta salads, candy etc.

Thank you and please do not hesitate to ask any questions.

www.belmaropizza.ca
www.peachnook.ca
Logo to be interchanged as they are affiliated meaning PeachNook is a brand within Belmaro pizza.

our target market is customers who have already entered our business. This is to upsel

We are in a self serve enviroment and target business people

• must be clean and catchy. We are located in a professional business community.
• Must be appealing, appetizing and utilize our website colors
• should not have any carton drawings and not be cluttered (busy)

```html
<!DOCTYPE html>
<html lang="en">
<head>
<meta charset="utf-8">
<title>What's for Dinner Tonight? – Take &amp; Bake Display</title>
<link rel="stylesheet" href="https://fonts.googleapis.com/css2?family=Montserrat:ital,wght@0,300;0,400;0,500;0,700;0,800;1,500;1,800&display=swap">
<style>
  :root {
    --navy: #0e1a40;
    --orange: #f05a28;
    --white: #ffffff;
    --stage: #e4e4e4;
    --photo-dark: #4a2620;
    --photo-mid: #7a3528;
    --photo-warm: #e0552d;
    --ink: #2b2b2b;
  }
  * { margin: 0; padding: 0; box-sizing: border-box; }
  html, body {
    width: 1199px;
    height: 1200px;
    overflow: hidden;
    background: var(--stage);
    font-family: "Montserrat", Arial, sans-serif;
  }
  .flyer {
    position: absolute;
    left: 167px;
    top: 40px;
    width: 642px;
    height: 832px;
    background: var(--white);
    overflow: hidden;
    transform: scale(1.3462);
    transform-origin: top left;
  }
  .flyer-shapes {
    position: absolute;
    inset: 0;
    width: 642px;
    height: 832px;
  }
  .brand-mark {
    position: absolute;
    left: 35px;
    top: 44px;
    width: 200px;
    text-align: center;
  }
  .brand-mark .dot {
    display: block;
    width: 66px;
    height: 66px;
    margin: 0 auto 10px;
    border-radius: 50%;
    border: 3px solid var(--navy);
  }
  .brand-mark .name {
    font-weight: 500;
    font-size: 24px;
    color: var(--navy);
    letter-spacing: 0.2px;
  }
  .headline {
    position: absolute;
    left: 55px;
    top: 250px;
    color: var(--white);
    line-height: 1;
  }
  .headline .lead {
    display: block;
    font-weight: 300;
    font-size: 50px;
    letter-spacing: 1px;
    margin-bottom: 14px;
  }
  .headline .main {
    display: block;
    font-weight: 800;
    font-size: 66px;
    letter-spacing: 1px;
    line-height: 1.03;
  }
  .menu-list {
    position: absolute;
    left: 57px;
    top: 484px;
    list-style: none;
    color: var(--white);
    font-weight: 700;
    font-size: 21px;
    line-height: 28px;
  }
  .price-tag {
    position: absolute;
    background: var(--white);
    color: var(--navy);
    font-weight: 800;
    font-style: italic;
    border-radius: 5px;
    box-shadow: 0 3px 8px rgba(0,0,0,0.35);
    display: flex;
    align-items: center;
    justify-content: center;
  }
  .price-tag.dinner {
    left: 420px;
    top: 508px;
    width: 152px;
    height: 50px;
    font-size: 30px;
  }
  .price-tag.snack {
    left: 52px;
    top: 710px;
    width: 153px;
    height: 50px;
    font-size: 18px;
  }
  .snack-copy {
    position: absolute;
    left: 55px;
    top: 638px;
    color: var(--white);
    font-style: italic;
    font-weight: 500;
    font-size: 12.5px;
    line-height: 17px;
  }
  .partner-name {
    position: absolute;
    left: 412px;
    top: 770px;
    font-weight: 400;
    font-size: 26px;
    color: var(--ink);
    letter-spacing: 0.5px;
  }
</style>
</head>
<body>
  <main class="flyer">
    <svg class="flyer-shapes" viewBox="0 0 642 832" aria-hidden="false">
      <defs>
        <radialGradient id="dish-tones" cx="0.78" cy="0.55" r="0.7">
          <stop offset="0" stop-color="var(--photo-warm)" stop-opacity="1"/>
          <stop offset="0.35" stop-color="#c8462a"/>
          <stop offset="0.7" stop-color="var(--photo-mid)"/>
          <stop offset="1" stop-color="var(--photo-dark)"/>
        </radialGradient>
      </defs>
      <path class="food-photo" role="img" aria-label="Close-up photo of freshly baked lasagna in a pan on a dark table"
            d="M0,236 Q250,140 642,150 L642,745 Q400,722 90,832 L0,832 Z"
            fill="url(#dish-tones)"/>
      <path class="top-band" d="M285,0 L642,0 L642,206 Q520,210 440,172 Q330,120 285,0 Z" fill="var(--navy)"/>
      <circle class="accent-dot" cx="392" cy="130" r="47" fill="var(--orange)" stroke="var(--white)" stroke-width="3"/>
      <path class="bottom-panel" d="M90,832 Q400,722 642,745 L642,832 Z" fill="var(--white)"/>
      <path class="bottom-stripe" d="M80,832 Q380,716 642,733 L642,745 Q400,724 106,832 Z" fill="var(--navy)"/>
    </svg>

    <div class="brand-mark">
      <span class="dot"></span>
      <span class="name">PeachNook</span>
    </div>

    <h1 class="headline">
      <span class="lead">WHAT'S FOR</span>
      <span class="main">DINNER</span>
      <span class="main">TONIGHT?</span>
    </h1>

    <ul class="menu-list">
      <li>* Take &amp; Bake"</li>
      <li>* "Baked Pasta"</li>
      <li>* Freshly made in house</li>
      <li>* Lasagna</li>
    </ul>

    <div class="price-tag dinner">$13.50</div>

    <p class="snack-copy">
      mini charcurterie board.<br>
      * snack size charcutier delight *<br>
      * Enjoy the flavors of gourment snacking, all in one convenient box!
    </p>

    <div class="price-tag snack">PRICE $8.99</div>

    <div class="partner-name">Belmaro Pizza</div>
  </main>
</body>
</html>
```